Redesign der Systemmails von motivhafen.de
Zielgruppe
Wir sind die Macher von motivhafen.de und wollen unsere Standardmails, die systemseitig verschickt werden, schöner und wertiger gestalten.
Aufgabenstellung
Wir sind der Meinung, dass unsere System-E-Mails ein Redesign nötig haben. Daher würden wir Dich bitten, uns Deinen Input zu geben. Die Mails sollen schlichter und moderner gestaltet werden. Folgende Elemente bedürfen aus unserer Sicht der Überarbeitung:
Schrift -> Aktuell verwenden wir Lucida Sans Unicode als Schrift für die Mails. Die Schrift passt aber nicht mehr so gut zur Seite. Auf der Seite verwenden wir inzwischen die Lato (leider keine Systemschrift).
Bitte schlage eine aus Deiner Sicht geeignete Systemschrift vor.
Buttonstyle -> Bitte einen frischen Buttonstyle vorschlagen
Schriftgröße und Farbe der Headline, des Fließtextes und des Footers -> Bitte harmonische Einteilung finden
Einen Screenshot einer aktuellen Mail ist anbei, außerdem einige Beispiele gelungener Mails anderer Unternehmen.
Die Datenlieferung sollte dann bitte als PSD und einer textlichen Beschreibung der Schriften, Schriftgrößen und Farbwerte erfolgen.
Bitte folgenden Text für die Gestaltung verwenden:
Hallo VORNAME NACHNAME,
Ihr Projekt 'BEISPIELPROJEKTTITEL' ist abgelaufen. Als nächstes sollten Sie ein Gewinner-Design bestimmen:
Button [Gewinner bestimmen]
Sie möchten noch Feinheiten am Design ändern lassen? Kein Problem: Finale Änderungen am Gewinnerdesign erledigt der Designer gerne im Rahmen der Datenübergabe. Küren Sie einfach Ihren Favoriten zum Gewinner und teilen Sie dem Designer Ihre Änderungswünsche in der Datenübergabe mit. Erst wenn Sie bestätigt haben, dass alle Daten mit den gewünschten Überarbeitungen vollständig übergeben wurden, wird das Preisgeld an den Designer transferiert.
Sie können sich zwischen Ihren Favoriten nicht entscheiden?
Kein Problem, nutzen Sie einfach unser praktisches Design-Voting und lassen Sie Familie, Freunde, Bekannte und Kollegen abstimmen. So sehen Sie, welches Design am besten ank..

```html
<!DOCTYPE html>
<html lang="de">
<head>
<meta charset="utf-8">
<title>motivhafen.de – Kommentar zum Projekt</title>
<link href="https://fonts.googleapis.com/css2?family=Arimo:wght@400;700&display=swap" rel="stylesheet">
<style>
  :root {
    --bg: #f4f4f4;
    --card: #ffffff;
    --text: #3a3a3a;
    --heading: #333333;
    --link: #1a8fc9;
    --button: #00c896;
    --button-text: #ffffff;
    --border: #e4e4e4;
    --muted: #8a8a8a;
  }
  * { box-sizing: border-box; margin: 0; padding: 0; }
  html, body {
    width: 1199px;
    height: 1200px;
    overflow: hidden;
    background: var(--bg);
    font-family: "Arimo", Arial, sans-serif;
    color: var(--text);
  }
  .mail {
    width: 1199px;
    height: 1200px;
    padding-top: 70px;
  }
  .brand {
    display: flex;
    align-items: center;
    justify-content: center;
    gap: 10px;
    height: 60px;
  }
  .brand-dot {
    width: 16px;
    height: 16px;
    background: var(--link);
  }
  .brand-name {
    font-size: 28px;
    font-weight: 400;
    color: var(--heading);
  }
  .card {
    width: 854px;
    margin: 30px auto 0;
    background: var(--card);
    padding: 74px 96px 72px;
    box-shadow: 0 12px 30px rgba(0,0,0,0.05);
    font-size: 18.5px;
    line-height: 30px;
  }
  .card a { color: var(--link); text-decoration: none; }
  .greeting { margin-bottom: 29px; }
  .comment {
    margin-top: 43px;
    border: 2px solid var(--border);
    border-radius: 3px;
    padding: 40px 58px 48px;
  }
  .comment-title {
    font-weight: 700;
    color: var(--heading);
    margin-bottom: 14px;
  }
  .notice { margin-top: 44px; }
  .cta {
    display: block;
    width: 192px;
    height: 48px;
    margin: 42px auto 0;
    background: var(--button);
    color: var(--button-text) !important;
    border-radius: 3px;
    text-align: center;
    line-height: 48px;
    font-weight: 700;
    font-size: 19px;
    box-shadow: 0 6px 14px rgba(0,0,0,0.12);
  }
  .signoff { margin-top: 42px; }
  .imprint {
    width: 854px;
    margin: 36px auto 0;
    padding: 0 96px;
    font-size: 13px;
    line-height: 22.5px;
    color: var(--muted);
  }
  .imprint-title { font-weight: 700; }
  .imprint a { color: var(--muted); }
</style>
</head>
<body>
<main class="mail">
  <header class="brand">
    <span class="brand-dot"></span>
    <span class="brand-name">motivhafen.de</span>
  </header>

  <section class="card">
    <p class="greeting">Hallo Jonas Beispiel,</p>
    <p class="intro">es wurde ein neuer Kommentar von Designer XYZ zum Design #2 im Projekt "Redesign der Website von <a href="#">Firma</a>" auf <a href="#">motivhafen.de</a> hinterlassen.</p>

    <div class="comment">
      <p class="comment-title">Kommentar:</p>
      <p class="comment-text">Lorem ipsum dolor sit amet, consetetur sadipscing elitr, sed diam nonumy eirmod tempor invidunt ut labore et dolore magna</p>
    </div>

    <p class="notice">Bitte nicht auf diese Email antworten, sondern direkt im Projekt!</p>

    <a class="cta" href="#">Zum Projekt</a>

    <p class="signoff">Viele Grüße, Ihr Team von <a href="#">motivhafen.de</a></p>
  </section>

  <footer class="imprint">
    <p class="imprint-title">Impressum</p>
    <p>motivhafen.de GmbH, Hafenweg 8, 20457 Musterstadt, Deutschland, +49 (0)40-5550123</p>
    <p>Geschäftsführer: Lena Albers und Tobias Reinhold, Amtsgericht Musterstadt: HRB 10203</p>
    <p>Sie können Ihre Maileinstellungen jederzeit ändern, indem Sie hier klicken:</p>
    <p><a href="#">https://www.motivhafen.de/konto/einstellungen</a></p>
  </footer>
</main>
</body>
</html>
```